Corvix Thinner Logo and Packaging Design

We are seeking a striking and professional logo and packaging design for our new product line, Corvix Thinner. This logo will be used on the packaging for three different sizes of half-transparent carboys: 1L, 4L, and 20L. Corvix Thinner is a high-quality solvent brand known for its excellent solvency, fast-drying properties, and pleasant smell. The logo should feature an eagle motif to symbolize power and precision, and our slogan, "POUR WITH PURITY." The design should be suitable for placement on hardware store and warehouse shelves. Additionally, we need the designer to create an eagle logo to accompany the packaging.

Packaging Dimensions:
1L Carboy:
Front: 71mm height x 142mm width
Side: 71mm height x 73mm width
4L Carboy:
Front: 160mm height x 170mm width
Side: 160mm height x 120mm width
20L Carboy:
Front: 245mm height x 190mm width
Side: 215mm height x 190mm width
Front Label Requirements:

Product Name: Thinner QZR
Volume: 20L
Precautionary Statements:
Keep Away from Sources of ignition - No Smoking
Avoid Contact with Eyes
Do Not Empty into Drains or Sewers
Take Precautionary Measures Against Static Discharge
Hazard Statements:
Flammable Liquid and Vapor
May be fatal if swallowed or enters Airways
Causes Skin Irritation
Causes Serious Eye Irritation
Causes Damage to Organs if Prolonged or Repeated Exposure
Hazard Pictograms: (Include relevant hazard symbols)
Design Requirements:

Logo: Eagle motif (to be designed by the designer)
Slogan: POUR WITH PURITY
Color Scheme: Designer to recommend (should be striking and professional for retail display)

Please see my latest picture. Kindly note the packaging is in Plastic Carboy (not in metal tin as per PS).

Eagle to be more majestic and bigger (as if soaring in the sky).
Singapore landscape as background to have Singapore identity such as KDT, Lumen Loop, terraces of mistral etc.

Eagle to be more majestic and bigger, wings to spread wide.
We not want it to be of photo style, but more on a cartoon style. Please see my latest file uploaded.

Target Market(s)

Our target market includes painting companies, construction companies, direct household consumers, and industrial users who require high-quality solvents for various applications.

Industry/Entity Type

Chemical, spray paint and painting, household, industrial

Requirements
Must have
• Professional and Striking Design: Eye-catching and professional packaging for retail shelves. Eagle Logo: A strong, precise eagle logo. Slogan: "POUR WITH PURITY" prominently displayed. Clear Precautionary and Hazard Statements: Important safety information and pictograms. Volume Indication: Clearly marked (e.g., 1L, 4L, 20L). Eagle to be more majestic and bigger (as if soaring in the sky). Singapore landscape as background to have Singapore identity such as KDT, Lumen Loop, terraces of mistral etc.
Nice to have
• Color Scheme Recommendations: Suggestions for a professional, striking color scheme. Versatility: Design elements adaptable across different sizes of packaging. Environmentally Friendly Elements: Indications of sustainability or eco-friendliness in the design.
Should not have
• Overly Complex Designs: Avoid cluttered or overly intricate designs that detract from readability. Inconsistent Branding: Ensure all elements are cohesive and align with the brand identity.

```html
<!DOCTYPE html>
<html lang="en">
<head>
<meta charset="utf-8">
<title>Corvix Thinner – Label Set</title>
<link rel="stylesheet" href="https://fonts.googleapis.com/css2?family=Montserrat:wght@500;600;800;900&display=swap">
<style>
  :root {
    --board: #c0bebe;
    --ink: #0d0d0d;
    --white: #ffffff;
    --green-a: #2ea85a;
    --green-b: #2ab0a6;
    --green-c: #2aaebe;
    --violet-a: #a57fc1;
    --violet-b: #8790cf;
    --violet-c: #6fa6df;
    --amber-a: #e7a04a;
    --coral-b: #e9806e;
    --pink-c: #ef7a92;
    --eco-green: #2fae72;
  }
  * { box-sizing: border-box; margin: 0; padding: 0; }
  html, body { width: 1200px; height: 569px; overflow: hidden; }
  body {
    background: var(--board);
    font-family: "Montserrat", sans-serif;
    color: var(--ink);
    position: relative;
  }
  .label {
    position: absolute;
    overflow: hidden;
    border-top: 7px solid var(--ink);
  }
  .label::after {
    content: "";
    position: absolute;
    inset: 0;
    background: linear-gradient(120deg, transparent 50%, rgba(255,255,255,.22) 50.2%, rgba(255,255,255,.05) 80%);
    pointer-events: none;
  }
  .label--20l {
    left: 282px; top: 88px; width: 314px; height: 406px;
    background: linear-gradient(165deg, var(--green-a) 0%, var(--green-b) 60%, var(--green-c) 100%);
  }
  .label--4l {
    left: 633px; top: 222px; width: 284px; height: 265px;
    background: linear-gradient(30deg, var(--violet-a) 0%, var(--violet-b) 45%, var(--violet-c) 100%);
  }
  .label--1l {
    left: 633px; top: 87px; width: 236px; height: 118px;
    background: linear-gradient(90deg, var(--amber-a) 0%, var(--coral-b) 50%, var(--pink-c) 100%);
    border-top-width: 4px;
  }
  .brand {
    position: absolute;
    display: flex;
    align-items: center;
    gap: 8px;
    font-weight: 800;
    white-space: nowrap;
    z-index: 1;
  }
  .brand__mark {
    width: 1.3em; height: 1.3em;
    background: var(--ink);
    border-radius: 50%;
  }
  .title {
    position: absolute;
    left: 0; right: 0;
    text-align: center;
    font-weight: 900;
    line-height: .88;
    letter-spacing: -.01em;
    z-index: 1;
  }
  .slogan {
    position: absolute;
    left: 0; right: 0;
    text-align: center;
    color: var(--white);
    font-weight: 900;
    white-space: nowrap;
    z-index: 1;
  }
  .pictograms {
    position: absolute;
    display: flex;
    z-index: 1;
  }
  .pictograms svg { display: block; }
  .safety {
    position: absolute;
    font-weight: 500;
    text-align: justify;
    z-index: 1;
  }
  .safety b { color: var(--white); font-weight: 800; }
  .volume-bar {
    position: absolute;
    right: 0;
    background: var(--ink);
    display: flex;
    align-items: center;
    justify-content: space-between;
    color: var(--white);
    font-weight: 900;
    z-index: 1;
  }
  .eco-badge {
    border-radius: 50%;
    border: 1.5px solid var(--eco);
    background: rgba(255,255,255,.04);
  }

  /* 20 L */
  .label--20l .brand { left: 34px; top: 34px; font-size: 20px; }
  .label--20l .title { top: 80px; font-size: 52px; }
  .label--20l .slogan { top: 180px; font-size: 24px; }
  .label--20l .pictograms { left: 22px; top: 248px; gap: 4px; }
  .label--20l .safety { left: 21px; right: 18px; top: 286px; font-size: 6.6px; line-height: 7.7px; }
  .label--20l .volume-bar { left: 17px; top: 335px; height: 57px; border-radius: 29px 0 0 29px; padding: 0 16px 0 12px; font-size: 33px; --eco: var(--eco-green); }
  .label--20l .eco-badge { width: 36px; height: 36px; }

  /* 4 L */
  .label--4l .brand { left: 48px; top: 20px; font-size: 16px; }
  .label--4l .title { top: 50px; font-size: 38px; }
  .label--4l .slogan { top: 121px; font-size: 20px; }
  .label--4l .pictograms { left: 22px; top: 147px; gap: 2px; }
  .label--4l .safety { left: 25px; right: 25px; top: 176px; font-size: 5.6px; line-height: 6.4px; }
  .label--4l .volume-bar { left: 14px; top: 213px; height: 44px; border-radius: 22px 0 0 22px; padding: 0 24px 0 12px; font-size: 28px; --eco: #9a83cc; }
  .label--4l .eco-badge { width: 29px; height: 29px; }

  /* 1 L */
  .label--1l .brand { left: 54px; top: 10px; font-size: 11px; }
  .label--1l .title { top: 32px; font-size: 26px; white-space: nowrap; }
  .label--1l .slogan { left: 30px; right: 0; top: 55px; font-size: 15px; }
  .label--1l .pictograms { left: 11px; top: 57px; flex-direction: column; gap: 0; }
  .label--1l .safety { left: 33px; width: 117px; top: 74px; font-size: 3.9px; line-height: 4.7px; }
  .label--1l .volume-bar { left: 153px; top: 82px; height: 28px; border-radius: 14px 0 0 14px; padding: 0 14px 0 4px; font-size: 16px; --eco: #f5a0ac; }
  .label--1l .eco-badge { width: 18px; height: 18px; }
</style>
</head>
<body>

<svg width="0" height="0" style="position:absolute" aria-hidden="true">
  <defs>
    <symbol id="ghs-flame" viewBox="0 0 40 40">
      <rect x="8" y="8" width="24" height="24" transform="rotate(45 20 20)" fill="none" stroke="#0d0d0d" stroke-width="2.6"/>
      <path d="M20 10c1 4 6 6 6 12a6 6 0 0 1-12 0c0-3 2-4 2-7 2 1 2 3 2 4 1-2 2-5 2-9z" fill="#0d0d0d"/>
      <rect x="13" y="28" width="14" height="1.8" fill="#0d0d0d"/>
    </symbol>
    <symbol id="ghs-exclaim" viewBox="0 0 40 40">
      <rect x="8" y="8" width="24" height="24" transform="rotate(45 20 20)" fill="none" stroke="#0d0d0d" stroke-width="2.6"/>
      <path d="M18 11h4l-.8 13h-2.4z" fill="#0d0d0d"/>
      <circle cx="20" cy="28" r="2.1" fill="#0d0d0d"/>
    </symbol>
    <symbol id="ghs-health" viewBox="0 0 40 40">
      <rect x="8" y="8" width="24" height="24" transform="rotate(45 20 20)" fill="none" stroke="#0d0d0d" stroke-width="2.6"/>
      <circle cx="20" cy="13" r="3" fill="#0d0d0d"/>
      <path d="M13 30c0-8 2-13 7-13s7 5 7 13z" fill="#0d0d0d"/>
      <path d="M20 20l1 3 3 .5-2.5 1.5 1 3-2.5-2-2.5 2 1-3-2.5-1.5 3-.5z" fill="#ffffff"/>
    </symbol>
  </defs>
</svg>

<!-- 20 L front label -->
<section class="label label--20l" aria-label="Corvix Thinner 20 litre label">
  <div class="brand"><span class="brand__mark"></span>CORVIX THINNER</div>
  <h1 class="title">THINNER<br>QZR</h1>
  <p class="slogan">POUR WITH PURITY</p>
  <div class="pictograms">
    <svg width="36" height="36"><use href="#ghs-flame"/></svg>
    <svg width="36" height="36"><use href="#ghs-exclaim"/></svg>
    <svg width="36" height="36"><use href="#ghs-health"/></svg>
  </div>
  <p class="safety"><b>PRECAUTIONS:</b> Keep Away from Sources of ignition - No Smoking.Avoid Contact with Eyes Do Not Empty into Drains or Sewers. Take Precautionary Measures Against Static Discharge. <b>HAZARDS:</b> Flammable Liquid and Vapor. May be fatal if swallowed or enters Airways. Causes Skin Irritation. Causes Serious Eye Irritation. Causes Damage to Organs if Prolonged or Repeated Exposure.</p>
  <div class="volume-bar"><span class="eco-badge" role="img" aria-label="Eco badge"></span><span class="volume">20 L</span></div>
</section>

<!-- 1 L front label -->
<section class="label label--1l" aria-label="Corvix Thinner 1 litre label">
  <div class="brand"><span class="brand__mark"></span>CORVIX THINNER</div>
  <h2 class="title">THINNER QZR</h2>
  <p class="slogan">POUR WITH PURITY</p>
  <div class="pictograms">
    <svg width="17" height="17"><use href="#ghs-flame"/></svg>
    <svg width="17" height="17"><use href="#ghs-exclaim"/></svg>
    <svg width="17" height="17"><use href="#ghs-health"/></svg>
  </div>
  <p class="safety"><b>PRECAUTIONS:</b> Keep Away from Sources of ignition - No Smoking.Avoid Contact with Eyes Do Not Empty into Drains or Sewers. Take Precautionary Measures Against Static Discharge. <b>HAZARDS:</b> Flammable Liquid and Vapor. May be fatal if swallowed or enters Airways. Causes Skin Irritation. Causes Serious Eye Irritation. Causes Damage to Organs if Prolonged or Repeated Exposure.</p>
  <div class="volume-bar"><span class="eco-badge" role="img" aria-label="Eco badge"></span><span class="volume">1 L</span></div>
</section>

<!-- 4 L front label -->
<section class="label label--4l" aria-label="Corvix Thinner 4 litre label">
  <div class="brand"><span class="brand__mark"></span>CORVIX THINNER</div>
  <h2 class="title">THINNER<br>QZR</h2>
  <p class="slogan">POUR WITH PURITY</p>
  <div class="pictograms">
    <svg width="30" height="30"><use href="#ghs-flame"/></svg>
    <svg width="30" height="30"><use href="#ghs-exclaim"/></svg>
    <svg width="30" height="30"><use href="#ghs-health"/></svg>
  </div>
  <p class="safety"><b>PRECAUTIONS:</b> Keep Away from Sources of ignition - No Smoking.Avoid Contact with Eyes Do Not Empty into Drains or Sewers. Take Precautionary Measures Against Static Discharge. <b>HAZARDS:</b> Flammable Liquid and Vapor. May be fatal if swallowed or enters Airways. Causes Skin Irritation. Causes Serious Eye Irritation. Causes Damage to Organs if Prolonged or Repeated Exposure.</p>
  <div class="volume-bar"><span class="eco-badge" role="img" aria-label="Eco badge"></span><span class="volume">4 L</span></div>
</section>

</body>
</html>
```